Nobre Lente Lusitana - business card

Create a business card for my eyewear (glasses) store. The concept is based in handcrafted glasses (as well as common frames and 3d printed), clean, and elegant. The business card could be black (white letters and symbols) or white (black letters and symbols) but we are open to new suggestions. It must be sober and elegant.
The name Nobre Lente Lusitana means Royal/Real Portuguese Optical Store.
Our concept should be inspired by the pictures attatched bellow.
I would like it to be classic and elegant as business cards for bankers.
Our first selected logo is also available in attachment files.

Target Market(s)

For business meetings with investors, supliers and fairs

Industry/Entity Type

Eyewear

Contact Information for Business Card

Some random business cards in attachment that we like. Don't be closed to it, we like freedom of think.

Font styles to use
Serif
Sans Serif

Colors
404040
e9e9e9
fbfbfb
000000
85abd3
0255a3
f7fbfd
959595

Requirements
Must have
• Must be elegant, simple.
• Must present our brand new logo (slight variations are welcome, the logo is not closed yet). See our temporary logo in attachment.
• Black (or dark grey), white (or light grey) and a third slight color.
• This third slight color could be dark blue or grayish blue.
• Info:
• Tomás Vidigal (name)
• tvidigal@nobrelentelusitana.example
• +351 927364051
• www.nobrelentelusitana.example
Nice to have
• Black and white or with serious colors such as dark blue or greyish blue.
• Could also have water mark with our logo (big size) in the background (inspired in KMT bank credit card design)
Should not have
• Hysteric colora or shapes

```html
<!DOCTYPE html>
<html lang="pt">
<head>
<meta charset="utf-8">
<title>Nobre Lente Lusitana – Cartão de visita</title>
<link rel="stylesheet" href="https://fonts.googleapis.com/css2?family=Jost:wght@400;600&display=swap">
<style>
  :root {
    --backdrop: #8e8e90;
    --card-white: #fbfbfb;
    --card-black: #050505;
    --ink: #000000;
    --ink-soft: #1a1a1a;
    --paper-text: #fbfbfb;
  }
  * { box-sizing: border-box; margin: 0; padding: 0; }
  html, body {
    width: 1200px;
    height: 638px;
    overflow: hidden;
  }
  body {
    background: var(--backdrop);
    font-family: "Jost", sans-serif;
    display: flex;
    align-items: center;
    justify-content: center;
    gap: 40px;
  }
  .card {
    width: 540px;
    height: 309px;
    position: relative;
    box-shadow: 0 6px 18px rgba(0,0,0,0.25);
  }
  .card--front {
    background: var(--card-white);
    color: var(--ink);
  }
  .card--back {
    background: var(--card-black);
    color: var(--paper-text);
  }

  .brand {
    position: absolute;
    display: flex;
    align-items: center;
    gap: 8px;
    white-space: nowrap;
  }
  .brand__square {
    width: 9px;
    height: 9px;
    background: currentColor;
    flex: none;
  }
  .brand__name {
    font-weight: 400;
    font-size: 14px;
    letter-spacing: 0.02em;
    line-height: 1;
  }
  .card--front .brand {
    left: 30px;
    top: 106px;
  }
  .card--back .brand {
    left: 60px;
    top: 96px;
  }

  .contact {
    position: absolute;
    left: 222px;
    top: 96px;
  }
  .contact__name {
    font-weight: 600;
    font-size: 23px;
    letter-spacing: 0.02em;
    margin-bottom: 14px;
  }
  .contact__line {
    font-size: 14px;
    color: var(--ink-soft);
    line-height: 1.9;
  }
</style>
</head>
<body>
  <section class="card card--front" aria-label="Frente do cartão">
    <div class="brand">
      <span class="brand__square"></span>
      <p class="brand__name">Nobre Lente Lusitana</p>
    </div>
    <div class="contact">
      <h1 class="contact__name">Tomás Vidigal</h1>
      <p class="contact__line">tvidigal@nobrelentelusitana.example</p>
      <p class="contact__line">+351 927364051</p>
      <p class="contact__line">www.nobrelentelusitana.example</p>
    </div>
  </section>

  <section class="card card--back" aria-label="Verso do cartão">
    <div class="brand">
      <span class="brand__square"></span>
      <p class="brand__name">Nobre Lente Lusitana</p>
    </div>
  </section>
</body>
</html>
```